International Technology Company Needs Cover Design

My company needs a Cover Design for my Every Door Swings Open online course. This course explains and demonstrates Exponential Technology and its effects on the Business Landscape. It serves Small and Medium Business owners.
This can be thought of as a Book Cover, but there is no physical book. It is a cover for delivery online. It may never physically exist. Similarly, it does not have to be limited to paper dimensions. Two of my examples are included: one as a book and one on an Vextra. I like the Globe/Planet analogy to illustrate how it is EVERY door swings open. Please ask any questions. Thank you.
Target Market(s)
Small and Medium Business Owners of non-Internet-centric companies; predominantly male; 40-55 yrs old
Industry/Entity Type
It Company
Other font styles liked:
- Make it work with the Design Sliders above.
Requirements
Must have
- Authority; Fonts that can be used online for consistency; web/video applicable color palette; Sense of Possibility and Innovation; Same Title; open to other Subtitle suggestions.)
Nice to have
- Innovation. Unique thought. Progression of technology/business/possibility.
Should not have
- Different Title. (Other Subtitles may be suggested.)

```html
<!DOCTYPE html>
<html lang="en">
<head>
<meta charset="utf-8">
<title>Every Door Swings Open — Online Course Cover</title>
<link href="https://fonts.googleapis.com/css2?family=Saira+Extra+Condensed:wght@600&family=Saira+Condensed:wght@500&family=Open+Sans:wght@400&family=Josefin+Sans:wght@400&display=swap" rel="stylesheet">
<style>
  :root {
    --paper-center: #ffffff;
    --paper-edge: #d2d4d6;
    --title-blue: #3e6b8f;
    --label-red: #c0100f;
    --label-text: #ffffff;
    --subtitle-grey: #76787a;
    --author-ink: #2b2b2b;
    --globe-light: #f2f3f4;
    --globe-mid: #a9adb1;
    --globe-dark: #55595d;
  }
  html, body {
    margin: 0;
    padding: 0;
    width: 800px;
    height: 1200px;
    overflow: hidden;
  }
  .cover {
    position: relative;
    width: 800px;
    height: 1200px;
    background: radial-gradient(ellipse 75% 60% at 50% 55%, var(--paper-center) 0%, #f1f2f3 55%, var(--paper-edge) 100%);
    overflow: hidden;
  }
  .title {
    position: absolute;
    left: 0;
    top: 0;
    width: 800px;
    height: 420px;
  }
  .title text {
    font-family: "Saira Extra Condensed", "Arial Narrow", sans-serif;
    font-weight: 600;
    fill: var(--title-blue);
  }
  .format-label {
    position: absolute;
    left: 273px;
    top: 421px;
    width: 252px;
    height: 46px;
    background: var(--label-red);
    color: var(--label-text);
    font-family: "Open Sans", sans-serif;
    font-size: 27px;
    line-height: 44px;
    text-align: center;
  }
  .subtitle {
    position: absolute;
    left: 0;
    top: 492px;
    width: 800px;
    margin: 0;
    text-align: center;
    font-family: "Saira Condensed", "Arial Narrow", sans-serif;
    font-weight: 500;
    font-size: 27px;
    line-height: 37px;
    letter-spacing: 4.2px;
    text-transform: uppercase;
    color: var(--subtitle-grey);
  }
  .globe {
    position: absolute;
    left: 208px;
    top: 686px;
    width: 374px;
    height: 374px;
    border-radius: 50%;
    background: radial-gradient(circle at 38% 30%, var(--globe-light) 0%, var(--globe-mid) 55%, var(--globe-dark) 100%);
  }
  .globe-shadow {
    position: absolute;
    left: 215px;
    top: 1038px;
    width: 360px;
    height: 44px;
    border-radius: 50%;
    background: radial-gradient(ellipse at center, rgba(0,0,0,0.3) 0%, rgba(0,0,0,0) 70%);
  }
  .author {
    position: absolute;
    left: 0;
    top: 1116px;
    width: 800px;
    margin: 0;
    text-align: center;
    font-family: "Josefin Sans", sans-serif;
    font-weight: 400;
    font-size: 42px;
    letter-spacing: 11px;
    color: var(--author-ink);
    text-transform: uppercase;
  }
</style>
</head>
<body>
  <main class="cover">
    <svg class="title" viewBox="0 0 800 420" role="heading" aria-level="1" aria-label="Every Door Swings Open">
      <text x="104" y="213" font-size="228" textLength="586" lengthAdjust="spacingAndGlyphs">EVERY DOOR</text>
      <text x="104" y="400" font-size="228" textLength="586" lengthAdjust="spacingAndGlyphs">SWINGS OPEN</text>
    </svg>

    <div class="format-label">online course</div>

    <p class="subtitle">The Business Owner’s Guide to<br>Reshaping Your Market with<br>Accelerating Technology<br>for Growth &amp; Gain</p>

    <div class="globe-shadow"></div>
    <div class="globe" role="img" aria-label="Silver metallic globe with raised continents"></div>

    <p class="author">Dorian M Halvers Jr</p>
  </main>
</body>
</html>
```